Box Design of "pet rapid test for dogs & cats" with professional use

"The market is in Southeast Asia, South America, Europe, and the U.S."
Clients: Veterinary clinics, pet hospitals,(a small number of home use)

Primary colors:
Orange, Green,or Blue, (select 1,or 2 color)
Neutrals: Black, Gray, or White (optional)
Dimensions:135mm(L)*90mm(W)*105mm(W)

Kindly review the attached file for additional content
Updates

I have increased my budget, please provide a satisfactory design solution, thank you very much for your work.

Target Market(s)

Southeast Asia, South America, Europe, and the U.S.

Industry/Entity Type

Veterinary test kit for dogs & cats

Colors
0054AA
0677BA
7BADD7
CADEEF
E8F1F8
0094D4
00A9DD
6FCCEA
C7EBF8
E9F6FB
00AB8E
00BBA5
67D7C9
C6EFE9
E9F9F6
59FF00
82FF00
B8FF75
E3FFCB
F4FFEA
F0912C
F2A743
F7CA91
FBE8D2
FDF5EE
EE7325
F08F49
F5BC92
FAE3D3
FDF4ED

Requirements
Nice to have
• Appealing Box Appearance with professional

```html
<!DOCTYPE html>
<html lang="en">
<head>
<meta charset="utf-8">
<title>Vetora Pet Rapid Test Kit – Box Panels</title>
<link href="https://fonts.googleapis.com/css2?family=Poppins:ital,wght@0,400;0,500;0,600;0,700;1,500&family=Ubuntu:wght@400;500&family=Oswald:wght@400;500;600&display=swap" rel="stylesheet">
<style>
  :root{
    --orange:#E2641F;
    --orange-deep:#C8561A;
    --orange-soft:#F08F49;
    --panel:#E9E9EA;
    --ink:#1E1E1E;
    --ink-soft:#3A3A3A;
    --white:#FFFFFF;
    --strip:#DCDCDD;
  }
  *{box-sizing:border-box;margin:0;padding:0}
  html,body{width:1200px;height:1200px;overflow:hidden;background:#F4F4F4}
  body{position:relative;font-family:"Poppins",sans-serif;color:var(--ink)}

  .panel{position:absolute;overflow:hidden}

  /* ---------- top panel ---------- */
  .top-panel{left:66px;top:100px;width:640px;height:427px;background:var(--panel)}
  .top-panel .brand{position:absolute;left:120px;top:110px;font-size:46px;font-weight:700;letter-spacing:2px}
  .top-panel .title{position:absolute;left:120px;top:180px;font-family:"Ubuntu",sans-serif;font-size:34px;letter-spacing:1px}
  .top-panel .subtitle{position:absolute;left:120px;top:222px;font-family:"Ubuntu",sans-serif;font-size:34px;color:var(--orange);font-weight:500}
  .top-panel .cross{position:absolute;right:60px;top:140px;width:80px;height:80px}
  .vet-band{position:absolute;left:0;bottom:0;width:100%;height:40px;background:var(--orange);color:var(--white);
    font-style:italic;font-weight:500;font-size:13px;letter-spacing:2px;padding:11px 0 0 74px}

  /* ---------- front panel ---------- */
  .front-panel{left:66px;top:527px;width:640px;height:500px;background:var(--panel)}
  .front-panel .brand{position:absolute;left:68px;top:62px;font-size:40px;font-weight:700;letter-spacing:1px;line-height:1}
  .front-panel .cross{position:absolute;left:514px;top:118px;width:88px;height:88px}
  .front-panel .title{position:absolute;left:54px;top:150px;font-family:"Ubuntu",sans-serif;font-size:44px;line-height:1;color:var(--ink)}
  .front-panel .subtitle{position:absolute;left:54px;top:198px;font-family:"Ubuntu",sans-serif;font-size:40px;line-height:1;font-weight:500;color:var(--orange)}
  .tagline{position:absolute;left:54px;top:252px;font-size:20px;font-weight:500;color:var(--ink-soft)}
  .contents{position:absolute;left:54px;top:304px;font-size:14px;color:var(--ink-soft)}
  .contents h3{font-weight:500;font-size:15px;margin-bottom:8px}
  .contents li{list-style:none;display:flex;align-items:center;gap:6px;height:22px;font-size:12.5px}
  .contents li svg{width:12px;height:14px;flex:none}
  .contents li .bar{width:1px;height:13px;background:var(--ink-soft)}

  .storage-band{position:absolute;left:0;top:428px;width:640px;height:72px;background:var(--orange)}
  .storage-band ul{position:absolute;left:50px;top:14px;list-style:none;color:var(--white);
    font-family:"Oswald",sans-serif;font-weight:500;font-size:15px;letter-spacing:.3px;line-height:24px}
  .storage-band li::before{content:"·";margin-right:10px}

  .pet-photo{position:absolute;left:330px;top:250px;width:310px;height:250px;
    background:radial-gradient(circle at 70% 40%,var(--orange-soft) 0 38%,var(--orange) 39% 60%,transparent 61%),
               linear-gradient(180deg,#D9A56A 0%,#B9824D 100%);
    border-top-left-radius:140px}

  /* ---------- side panel ---------- */
  .side-panel{left:706px;top:527px;width:427px;height:500px;background:var(--orange);color:var(--white)}
  .side-panel .es-title{position:absolute;left:28px;top:42px;width:300px;font-family:"Oswald",sans-serif;font-weight:400;font-size:24px;line-height:1.25}
  .side-panel .es-tag{position:absolute;left:28px;top:116px;width:250px;font-size:14px;line-height:1.4}
  .side-panel .es-contents{position:absolute;left:28px;top:186px;font-family:"Oswald",sans-serif;font-size:22px}
  .icon-grid{position:absolute;left:28px;top:236px;display:grid;grid-template-columns:92px 92px;row-gap:22px;column-gap:18px}
  .icon-item{text-align:center;font-size:11px}
  .icon-item .ring{width:58px;height:58px;border:1.5px solid var(--white);border-radius:50%;margin:0 auto 6px;display:flex;align-items:center;justify-content:center}
  .icon-item .ring svg{width:24px;height:28px}
  .icon-item small{display:block;font-size:6px;line-height:1.2;opacity:.9}
  .side-strip{position:absolute;left:330px;top:160px;width:52px;height:270px;background:var(--strip);border-radius:6px;
    display:flex;align-items:center;justify-content:center}
  .side-strip p{transform:rotate(-90deg);white-space:nowrap;color:var(--ink);font-family:"Oswald",sans-serif;font-weight:600;font-size:10px;line-height:1.5;text-align:center}
</style>
</head>
<body>

  <!-- top panel -->
  <section class="panel top-panel">
    <div class="brand">VETORA</div>
    <div class="title">PET RAPID TEST KIT</div>
    <div class="subtitle">for Dogs &amp; Cats</div>
    <svg class="cross" viewBox="0 0 100 100" aria-hidden="true">
      <path d="M35 5h30v30h30v30h-30v30h-30v-30h-30v-30h30z" fill="var(--orange)"/>
      <path d="M43 20h14v23h23v14h-23v23h-14v-23h-23v-14h23z" fill="var(--white)"/>
    </svg>
    <div class="vet-band">FOR VET USE ONLY</div>
  </section>

  <!-- front panel -->
  <section class="panel front-panel">
    <div class="brand">VETORA</div>
    <svg class="cross" viewBox="0 0 100 100" aria-hidden="true">
      <path d="M35 5h30v30h30v30h-30v30h-30v-30h-30v-30h30z" fill="var(--orange)"/>
      <path d="M43 20h14v23h23v14h-23v23h-14v-23h-23v-14h23z" fill="var(--white)"/>
    </svg>
    <h1 class="title">PET RAPID TEST KIT</h1>
    <h2 class="subtitle">for Dogs &amp; Cats</h2>
    <p class="tagline">Loved by Pets, Trusted by Vets</p>

    <div class="contents">
      <h3>Contents:</h3>
      <ul>
        <li><svg viewBox="0 0 12 14"><path d="M8 1l3 3-6 8-3-3z" fill="var(--orange)"/></svg><span class="bar"></span>Test Kit (Cassette, dropper, desiccant)</li>
        <li><svg viewBox="0 0 12 14"><rect x="4" y="0" width="4" height="3" fill="var(--orange)"/><rect x="2" y="3" width="8" height="11" rx="2" fill="var(--orange)"/></svg><span class="bar"></span>Assay buffer</li>
        <li><svg viewBox="0 0 12 14"><circle cx="6" cy="7" r="5" fill="var(--orange)"/></svg><span class="bar"></span>Sterile swabs</li>
        <li><svg viewBox="0 0 12 14"><path d="M1 0h7l3 3v11h-10z" fill="var(--orange)"/><path d="M3 6h6M3 9h6" stroke="var(--white)"/></svg><span class="bar"></span>Instruction manual</li>
      </ul>
    </div>

    <div class="storage-band">
      <ul>
        <li>STORAGE: 2~30 C° – AVOID SUNLIGHT</li>
        <li>10 TESTS / BOX</li>
      </ul>
    </div>

    <div class="pet-photo" role="img" aria-label="Photo of a tabby cat and a smiling golden retriever in front of an orange circle"></div>
  </section>

  <!-- side panel -->
  <section class="panel side-panel">
    <h2 class="es-title">KIT DE PRUEBA RÁPIDA PARA MASCOTAS (Perros y Gatos)</h2>
    <p class="es-tag">Querido por las mascotas, confiado por veterinarios</p>
    <p class="es-contents">Contenido:</p>
    <div class="icon-grid">
      <div class="icon-item">
        <div class="ring"><svg viewBox="0 0 24 28"><path d="M16 2l5 5-12 16-5-5z" fill="none" stroke="var(--white)" stroke-width="2"/></svg></div>
        Kit de prueba<small>casete, gotero, desecante</small>
      </div>
      <div class="icon-item">
        <div class="ring"><svg viewBox="0 0 24 28"><rect x="9" y="1" width="6" height="5" fill="var(--white)"/><rect x="6" y="6" width="12" height="20" rx="3" fill="var(--white)"/></svg></div>
        Buffer de ensayo
      </div>
      <div class="icon-item">
        <div class="ring"><svg viewBox="0 0 24 28"><circle cx="12" cy="14" r="8" fill="var(--white)"/></svg></div>
        Hisoposestériles
      </div>
      <div class="icon-item">
        <div class="ring"><svg viewBox="0 0 24 28"><path d="M4 2h11l5 5v19h-16z" fill="var(--white)"/><path d="M7 12h10M7 16h10M7 20h10" stroke="var(--orange)" stroke-width="1.5"/></svg></div>
        Kit de prueba
      </div>
    </div>
    <div class="side-strip">
      <p>2~30C° – EVITAR LA LUZ SOLAR DIRECTA<br>10 PRUEBAS POR CAJAD</p>
    </div>
  </section>

</body>
</html>
```